Appraisal and Umpire Services for Property Damage Insurance Claims

I need a banner design that I can post as an advertisement on industry web pages. I would like this to be elegant and reflective of quality, integrity and professionalism.

Target Market(s)

Insurance Companies and Attorneys

Industry/Entity Type

Insurance

Contact Information for Business Card

Gerald M. Hollis
918 Birchwell Lane
PO Box 582
Clifton Park, NY 12093
ghollis@brindlevault.com
Phone: (800) 555-0147, Ext. 2861
Direct: (315) 555-0189

Logo Text

Line One: Velmar Brook Claim Service, Inc. Line two: Appraisal and Umpire Services

Font styles to use
Serif
Sans Serif

Colors
0255a3
f78f20
faa54b
3176b5

Requirements
Must have
• New Logo and matching banner, business card and stationary.
• The colors must be orange and navy blue in the logo. I have selected them below.

```html
<!DOCTYPE html>
<html lang="en">
<head>
<meta charset="utf-8">
<title>Velmar Brook Claim Service, Inc. – Stationery Set</title>
<link rel="stylesheet" href="https://fonts.googleapis.com/css2?family=Raleway:wght@400&family=Open+Sans:wght@400;700&display=swap">
<style>
  :root {
    --navy: #0255a3;
    --orange: #f78f20;
    --orange-light: #faa54b;
    --blue-mid: #3176b5;
    --paper: #ffffff;
    --backdrop: #e2e2e2;
    --ink: #3a3a3a;
  }
  html, body { margin: 0; padding: 0; overflow: hidden; }
  body { width: 1200px; height: 640px; background: var(--backdrop); }
  .stationery-set { position: relative; width: 1200px; height: 640px; overflow: hidden; background: var(--backdrop); }

  .sheet { position: absolute; box-shadow: 0 2px 6px rgba(0,0,0,0.18); }

  .brand { display: flex; align-items: center; gap: 6px; font-family: "Raleway", sans-serif; font-weight: 400; white-space: nowrap; }
  .brand-dot { flex: none; border-radius: 50%; background: var(--orange); }
  .brand-text { display: flex; flex-direction: column; line-height: 1; }
  .brand-sub { align-self: flex-end; }

  .brand--light { color: var(--paper); }
  .brand--navy { color: var(--navy); }

  .contact { font-family: "Open Sans", sans-serif; font-style: normal; font-weight: 400; line-height: 1.2; white-space: nowrap; }
  .contact-label { font-weight: 700; }

  /* Blue folder sheet */
  .folder-sheet { left: 60px; top: 100px; width: 296px; height: 450px; background: var(--navy); }
  .folder-sheet .brand { position: absolute; left: 70px; bottom: 34px; gap: 5px; }
  .folder-sheet .brand-dot { width: 18px; height: 18px; }
  .folder-sheet .brand-name { font-size: 14px; }
  .folder-sheet .brand-sub { font-size: 5px; margin-top: 2px; }

  /* Letterhead */
  .letterhead { left: 270px; top: 157px; width: 296px; height: 415px; background: var(--paper); }
  .letterhead .brand { position: absolute; right: 22px; top: 22px; }
  .letterhead .brand-dot { width: 19px; height: 19px; }
  .letterhead .brand-name { font-size: 15px; }
  .letterhead .brand-sub { font-size: 5px; margin-top: 2px; }
  .letterhead .contact { position: absolute; left: 17px; bottom: 17px; font-size: 5.2px; color: var(--blue-mid); }
  .letterhead .contact-label { color: var(--navy); }

  /* Envelope */
  .envelope { left: 592px; top: 47px; width: 328px; height: 126px; background: var(--navy); box-shadow: none; }
  .envelope .brand { position: absolute; left: 16px; bottom: 11px; gap: 5px; }
  .envelope .brand-dot { width: 17px; height: 17px; }
  .envelope .brand-name { font-size: 12px; }
  .envelope .brand-sub { font-size: 4px; margin-top: 2px; }
  .envelope .contact { position: absolute; left: 250px; bottom: 12px; font-size: 4px; color: var(--paper); opacity: 0.85; }

  /* Business card */
  .business-card { left: 682px; top: 312px; width: 270px; height: 155px; background: var(--paper); }
  .business-card .brand { position: absolute; right: 27px; top: 26px; }
  .business-card .brand-dot { width: 34px; height: 34px; }
  .business-card .brand-name { font-size: 21px; }
  .business-card .brand-sub { font-size: 6px; margin-top: 2px; color: var(--blue-mid); }
  .business-card .contact { position: absolute; left: 15px; bottom: 14px; font-size: 7px; color: var(--ink); }
  .business-card .contact-label { color: #111; }
</style>
</head>
<body>
<main class="stationery-set">

  <section class="sheet folder-sheet" aria-label="Presentation folder">
    <div class="brand brand--light">
      <span class="brand-dot"></span>
      <span class="brand-text"><span class="brand-name">Velmar Brook</span><span class="brand-sub">Claim Service, Inc</span></span>
    </div>
  </section>

  <section class="sheet letterhead" aria-label="Letterhead">
    <div class="brand brand--navy">
      <span class="brand-dot"></span>
      <span class="brand-text"><span class="brand-name">Velmar Brook</span><span class="brand-sub">Claim Service, Inc</span></span>
    </div>
    <address class="contact">
      <span class="contact-label">Contact</span><br>
      Gerald M. Hollis<br>
      Email: ghollis@brindlevault.com<br>
      Phone: (800) 555-0147, Ext. 2861
    </address>
  </section>

  <section class="sheet envelope" aria-label="Envelope">
    <div class="brand brand--light">
      <span class="brand-dot"></span>
      <span class="brand-text"><span class="brand-name">Velmar Brook</span><span class="brand-sub">Claim Service, Inc</span></span>
    </div>
    <address class="contact">
      <span class="contact-label">Contact</span><br>
      Gerald M. Hollis<br>
      Email: ghollis@brindlevault.com<br>
      Phone: (800) 555-0147, Ext. 2861
    </address>
  </section>

  <section class="sheet business-card" aria-label="Business card">
    <div class="brand brand--navy">
      <span class="brand-dot"></span>
      <span class="brand-text"><span class="brand-name">Velmar Brook</span><span class="brand-sub">Claim Service, Inc</span></span>
    </div>
    <address class="contact">
      <span class="contact-label">Contact</span><br>
      Gerald M. Hollis<br>
      Email: ghollis@brindlevault.com<br>
      Phone: (800) 555-0147, Ext. 2861
    </address>
  </section>

</main>
</body>
</html>
```